Magnetic Business card Design do a service provider

Hi,

The company aim is to provide all service needs under one roof. However, at the moment there is only Accounting, Electrical and IT branches. There will be more services coming onboard in the future.

I already have a logo designed (Company name is already part of the logo), I now need a magnetic business card designed.

The business card will contain the following:

- Company Logo
- Contact#
- E-mail
- enough space to add website URL (for future)
Updates

Project Deadline Extended Reason: HI All,The deadline has been extended due to not having enough time to review an overwhelming number of designs that has been submitted by lots of designers.I will be uploading a draft of designs that i have in mind.Thanks. Added Friday, January 22, 2016

Target Market(s)

Residential, Home-based Businesses, Small and Medium businesses

Industry/Entity Type

Business

Contact Information for Business Card

Contact#: 0491 738 520
E-mail: service@brightlanetrades.net.au

Font styles to use
Decorative
Script

Requirements
Must have
• Round edges
• Some form of logo incorporation as a background

```html
<!DOCTYPE html>
<html lang="en">
<head>
<meta charset="utf-8">
<title>Bright Lane Trades – Business Card</title>
<link rel="stylesheet" href="https://fonts.googleapis.com/css2?family=Open+Sans:wght@400&family=Playfair+Display:ital,wght@1,600&display=swap">
<style>
  :root {
    --page-bg: #1a1a1c;
    --card-bg-top: #3a3b3d;
    --card-bg-bottom: #1f2022;
    --card-edge: #8f9698;
    --gold: #d8ad57;
    --gold-light: #f0cf86;
    --gold-dark: #a9802f;
    --icon-ink: #1f2022;
  }
  * { margin: 0; padding: 0; box-sizing: border-box; }
  html, body {
    width: 1200px; height: 855px; overflow: hidden;
    background: var(--page-bg);
  }
  .card {
    position: absolute;
    left: 120px; top: 147px;
    width: 960px; height: 560px;
    border-radius: 28px;
    background: linear-gradient(160deg, var(--card-bg-top) 0%, var(--card-bg-bottom) 100%);
    border: 2px solid var(--card-edge);
    overflow: hidden;
    font-family: "Open Sans", sans-serif;
    color: var(--gold);
  }
  .card__swoosh { position: absolute; inset: 0; }
  .brand {
    position: absolute;
    right: 44px; top: 70px;
    display: flex; align-items: center; gap: 14px;
  }
  .brand__dot {
    width: 24px; height: 24px; border-radius: 50%;
    background: var(--gold);
  }
  .brand__name {
    font-size: 32px; font-weight: 400; color: var(--gold);
    letter-spacing: 0.5px;
    white-space: nowrap;
  }
  .contacts {
    position: absolute;
    right: 44px; top: 245px;
    display: flex; flex-direction: column; align-items: flex-end; gap: 10px;
  }
  .contact-row {
    display: flex; align-items: center; gap: 14px;
    font-size: 23px; letter-spacing: 0.3px;
    white-space: nowrap;
  }
  .contact-icon {
    width: 22px; height: 22px; border-radius: 3px;
    background: var(--gold);
    display: flex; align-items: center; justify-content: center;
  }
  .contact-icon svg { width: 15px; height: 15px; }
  .person {
    position: absolute;
    left: 150px; top: 440px;
  }
  .person__name {
    font-family: "Playfair Display", serif;
    font-style: italic; font-weight: 600;
    font-size: 40px; line-height: 1.15; color: var(--gold-light);
    letter-spacing: 1px;
    white-space: nowrap;
  }
  .person__role {
    font-size: 22px; color: var(--gold);
    margin-top: 2px;
  }
</style>
</head>
<body>
  <div class="card">
    <svg class="card__swoosh" viewBox="0 0 960 560" aria-hidden="true">
      <defs>
        <linearGradient id="swoosh-gold" x1="0" y1="1" x2="1" y2="0">
          <stop offset="0" stop-color="#f0cf86"/>
          <stop offset="0.5" stop-color="#d8ad57"/>
          <stop offset="1" stop-color="#a9802f"/>
        </linearGradient>
      </defs>
      <path d="M0 470 C 150 380, 330 350, 420 290 C 480 245, 505 150, 520 0
               L 528 0 C 512 155, 478 258, 428 310 C 330 378, 160 412, 0 510 Z"
            fill="url(#swoosh-gold)"/>
    </svg>

    <div class="brand">
      <span class="brand__dot"></span>
      <span class="brand__name">Bright Lane Trades</span>
    </div>

    <div class="contacts">
      <div class="contact-row">
        <span>0491 738 520</span>
        <span class="contact-icon">
          <svg viewBox="0 0 16 16"><path d="M4 1h3l1 4-2 1a8 8 0 0 0 4 4l1-2 4 1v3c0 1-1 2-2 2C7 14 2 9 2 3c0-1 1-2 2-2z" fill="var(--icon-ink)"/></svg>
        </span>
      </div>
      <div class="contact-row">
        <span>www.brightlanetrades.net.au</span>
        <span class="contact-icon">
          <svg viewBox="0 0 16 16" fill="none" stroke="var(--icon-ink)" stroke-width="1.5"><circle cx="8" cy="8" r="6"/><path d="M2 8h12M8 2c3 3 3 9 0 12M8 2c-3 3-3 9 0 12"/></svg>
        </span>
      </div>
      <div class="contact-row">
        <span>service@brightlanetrades.net.au</span>
        <span class="contact-icon">
          <svg viewBox="0 0 16 16" fill="none" stroke="var(--icon-ink)" stroke-width="1.5"><rect x="2" y="4" width="12" height="9"/><path d="M2 4l6 5 6-5"/></svg>
        </span>
      </div>
    </div>

    <div class="person">
      <div class="person__name">Daniel R. Whitmore</div>
      <div class="person__role">President</div>
    </div>
  </div>
</body>
</html>
```